Brell Harbor Company Business Cards

Front and Back Business Card - logo and text setup - cool design. I need workable photoshop or illustrator files so I can setup each employee card with design that is created
Updates

Hi everyone, thank you for the great entries. Please no more white and blue cards - there are so many already - black and silver only now please. thanks!

Target Market(s)

Construction Industry - Facility Managers

Industry/Entity Type

Construction

Contact Information for Business Card

I really like contemporary simplistic looks - clean neat....not opposed to seeing some black backrounds

Requirements
Must have
• Logo/website address with design on front only - www.brellharbor-example.com (logo attached)
• Back:
• Name/Title/Company Address/Phone/email address
Nice to have
• Cool design
Should not have
• Nothing gimmicky like Fire or Water - since we are a Fire Protection company - it has all been done

```html
<!DOCTYPE html>
<html lang="en">
<head>
<meta charset="utf-8">
<title>Brell Harbor Company – Business Cards</title>
<link rel="stylesheet" href="https://fonts.googleapis.com/css2?family=Maven+Pro:wght@400;500;700&display=swap">
<style>
  :root {
    --stage: #1a1a1a;
    --card-dark: #141414;
    --card-light: #ffffff;
    --navy: #233a70;
    --flame: #f04a30;
    --salmon: #f58a68;
    --ink: #1e1e1e;
    --pale: #e6e6e6;
  }
  * { box-sizing: border-box; margin: 0; padding: 0; }
  html, body { width: 1200px; height: 1000px; overflow: hidden; }
  body {
    position: relative;
    background: var(--stage);
    font-family: "Maven Pro", "Helvetica Neue", Arial, sans-serif;
  }
  .card { position: absolute; width: 650px; height: 370px; overflow: hidden; }

  /* Front */
  .card--front { left: 275px; top: 87px; background: var(--card-dark); }
  .front-name {
    position: absolute; left: 0; right: 0; top: 166px;
    text-align: center; font-size: 30px; font-weight: 700;
    color: var(--salmon); letter-spacing: 1px;
  }
  .front-web {
    position: absolute; left: 0; right: 0; top: 325px;
    text-align: center; font-size: 15px; font-weight: 400;
    color: var(--pale); letter-spacing: 5px;
  }

  /* Back */
  .card--back { left: 273px; top: 528px; background: var(--card-light); }
  .brand-name {
    position: absolute; left: 60px; top: 152px;
    font-size: 34px; font-weight: 700; color: var(--navy);
  }
  .person { position: absolute; left: 379px; top: 80px; }
  .person__name { font-size: 23px; color: var(--flame); font-weight: 400; line-height: 1.1; }
  .person__name strong { color: var(--navy); font-weight: 700; }
  .person__role { font-size: 15px; color: var(--ink); margin-top: 4px; }
  .person__role span { color: var(--flame); font-weight: 500; }

  .contacts { position: absolute; left: 378px; top: 146px; list-style: none; }
  .contacts li {
    display: flex; align-items: center; height: 26px;
    font-size: 16px; color: var(--ink);
  }
  .contacts svg { width: 18px; height: 18px; margin-right: 10px; fill: var(--navy); flex: none; }

  .address-band {
    position: absolute; left: 0; right: 0; top: 314px; height: 32px;
    background: var(--flame); color: #fff; font-size: 16px;
    display: flex; align-items: center; justify-content: center;
  }
</style>
</head>
<body>
  <section class="card card--front" aria-label="Card front">
    <div class="front-name">Brell Harbor</div>
    <div class="front-web">WWW.BRELLHARBOR-EXAMPLE.COM</div>
  </section>

  <section class="card card--back" aria-label="Card back">
    <div class="brand-name">brellharbor</div>

    <div class="person">
      <div class="person__name"><strong>WADE</strong> renner</div>
      <div class="person__role">CEO of <span>brellharbor.co</span></div>
    </div>

    <ul class="contacts">
      <li>
        <svg viewBox="0 0 24 24" aria-hidden="true"><path d="M6.6 10.8c1.4 2.8 3.8 5.1 6.6 6.6l2.2-2.2c.3-.3.7-.4 1-.2 1.1.4 2.3.6 3.6.6.6 0 1 .4 1 1V20c0 .6-.4 1-1 1C10.6 21 3 13.4 3 4c0-.6.4-1 1-1h3.5c.6 0 1 .4 1 1 0 1.3.2 2.5.6 3.6.1.3 0 .7-.2 1z"/></svg>
        (02) 5550 1234
      </li>
      <li>
        <svg viewBox="0 0 24 24" aria-hidden="true"><path d="M7 1h10a2 2 0 0 1 2 2v18a2 2 0 0 1-2 2H7a2 2 0 0 1-2-2V3a2 2 0 0 1 2-2zm0 3v14h10V4zm5 15.5a1.2 1.2 0 1 0 0 2.4 1.2 1.2 0 0 0 0-2.4z"/></svg>
        0400 555 012
      </li>
      <li>
        <svg viewBox="0 0 24 24" aria-hidden="true"><path d="M2 5h20v14H2zm2 2v.5l8 5 8-5V7zm0 2.8V17h16V9.8l-8 5z"/></svg>
        info@brellharbor-example.com
      </li>
      <li>
        <svg viewBox="0 0 24 24" aria-hidden="true"><path d="M12 2a10 10 0 1 0 0 20 10 10 0 0 0 0-20zm-1 17.9A8 8 0 0 1 4.1 10L9 15v1c0 1.1.9 2 2 2zm6.9-2.5A2 2 0 0 0 16 16h-1v-3c0-.6-.4-1-1-1H8v-2h2c.6 0 1-.4 1-1V7h2c1.1 0 2-.9 2-2v-.4a8 8 0 0 1 2.9 12.8z"/></svg>
        www.brellharbor-example.com
      </li>
    </ul>

    <div class="address-band">118/4 Quay Lane, Marlow, NSW 2999</div>
  </section>
</body>
</html>
```